Curl Radiant through and through. Hair stylist that specializes in extensions.

I am Marisol I am a hair stylist and I would like a website designed for my hair business.

I currently book clients via my profile on trimnook.example/marisolbrantley

I need a professional website ( curlradiantthroughandthrough.example ) to display photos and prices for services offered.

I would like to have a home page with a brief bio, Image with logo and testimonials at the bottom, and a header with tab that include: menu of services, gallery,and FAQs.

On the "Services" page, I'm not interested in photos on this page. Just the name of the service, brief description, and pricing. I would also like to have, on this page, "Appointment Request" with fields that include: Name, service requested, desired time frame (morning, afternoon, evening), and contact number and email

On the "Gallery" page, I would like pictures only, but arranged and/or presented in a creative way...

Target Market(s)

Women ages 25-55 who interested in hair extension services.

Industry/Entity Type

Hair And Beauty

Coding

Number of Pages Required

5+ page

Font styles to use
Sans Serif

Requirements
Must have
• Must include tabs that include, Menu of services offered, a quick fund link to pay deposits with ease, location, contact information, photo gallery, and policy/faqs.
Nice to have
• If possible i would like to stream music with the ability to be silenced. I would like a neutral color palette tans and beige.
Should not have
• stock images

```html
<!DOCTYPE html>
<html lang="en">
<head>
<meta charset="utf-8">
<title>Curl Radiant through and through</title>
<link href="https://fonts.googleapis.com/css2?family=Lato:wght@400;700;900&family=Raleway:wght@500;600;700&family=Great+Vibes&display=swap" rel="stylesheet">
<style>
:root{
  --ink:#222226;
  --text:#666;
  --muted:#888;
  --dark:#39383d;
  --charcoal:#333336;
  --orange:#c97d1c;
  --white:#fff;
  --panel:#f2f2f2;
  --line:#cfcfcf;
  --navy:#1c2b4a;
  --friend:#1f70d6;
  --chirp:#1da1e2;
  --link:#1f4f66;
  --snap:#d22b3b;
}
*{box-sizing:border-box;margin:0;padding:0}
html,body{width:1200px;height:2927px;overflow:hidden}
body{position:relative;background:var(--white);font-family:"Lato",sans-serif;color:var(--text)}
.abs{position:absolute}
/* header */
.site-header{left:0;top:0;width:1200px;height:90px;background:var(--white)}
.brand{left:66px;top:24px;white-space:nowrap}
.brand-name{font:900 24px/1 "Lato",sans-serif;color:var(--ink);letter-spacing:1px}
.brand-sub{font:400 10px/1 "Lato",sans-serif;color:var(--ink);letter-spacing:2px;margin-top:6px;text-transform:uppercase}
.main-nav{left:351px;top:0;height:90px;display:flex}
.main-nav a{display:block;height:90px;font:700 12px/90px "Lato",sans-serif;padding:0 20px;color:var(--ink);text-decoration:none;text-transform:uppercase}
.main-nav a.active{background:var(--charcoal);color:var(--white);padding:0 19px}
.fund-btn{left:946px;top:18px;width:134px;height:52px;background:var(--orange);color:var(--white);font:900 21px/52px "Lato",sans-serif;text-align:center}
/* hero */
.hero{left:0;top:90px;width:1200px;height:681px;background:linear-gradient(90deg,#8a6a4e 0%,#b08a66 20%,#7a5c44 38%,#4a4a4a 60%,#3a3a3a 100%)}
.hero-title{right:26px;top:268px;width:560px;text-align:right;font:400 58px/1.15 "Great Vibes",cursive;color:var(--white)}
.hero-copy{right:36px;top:418px;width:560px;text-align:right;font:400 13.5px/22px "Lato",sans-serif;color:var(--white)}
.hero-btn{left:946px;top:503px;width:182px;height:57px;background:var(--orange);color:var(--white);font:400 18px/57px "Lato",sans-serif;text-align:center;border-radius:3px}
.dots{left:922px;top:601px;display:flex;gap:17px;align-items:center}
.dots span{width:14px;height:14px;border-radius:50%;background:var(--white)}
.dots span.on{width:24px;height:24px;background:none;border:3px solid var(--white)}
.dots span.on::after{content:"";display:block;width:10px;height:10px;margin:4px;border-radius:50%;background:var(--white)}
/* bio */
.bio{left:45px;top:665px;width:1110px;height:223px;background:var(--dark)}
.bio h2{position:absolute;left:39px;top:28px;font:500 24px "Raleway",sans-serif;color:var(--white)}
.bio p{position:absolute;left:39px;top:80px;width:760px;font:400 11.5px/25px "Lato",sans-serif;color:#d0d0d0}
.bio-more{display:inline-block;width:13px;height:13px;border-radius:50%;background:var(--white);vertical-align:middle;margin-left:6px}
.bio-portrait{left:856px;top:22px;width:172px;height:179px;background:linear-gradient(135deg,#d9a36a,#8a5a3a 60%,#f5f5f5);border:4px solid #e8e8e8}
/* welcome */
.section-title{left:0;width:1200px;text-align:center;font:600 32px "Raleway",sans-serif;color:var(--ink)}
.welcome-copy{left:100px;top:986px;width:1000px;text-align:center;font:400 11.5px/20px "Lato",sans-serif;color:var(--muted)}
.dark-btn{background:var(--charcoal);color:var(--white);text-align:center;font-family:"Lato",sans-serif;font-weight:700;font-size:11px;text-transform:uppercase}
/* booking */
.booking{left:0;top:1173px;width:1200px;height:462px;background:linear-gradient(90deg,#c9a888 0%,#a08a7c 30%,#9c8f8a 60%,#b48e6a 100%)}
.book-panel{left:119px;top:1284px;width:952px;height:289px;background:rgba(8,8,8,.9)}
.book-pointer{left:502px;top:1284px;width:0;height:0;border-left:10px solid transparent;border-right:10px solid transparent;border-top:11px solid var(--white)}
.tabs{left:480px;top:1306px;display:flex;font:700 12px/20px "Lato",sans-serif;color:var(--white)}
.tabs span{padding:0 22px;border-left:1px solid #999}
.tabs span:first-child{border-left:none;color:var(--orange);padding-left:0}
.service-photo{left:211px;top:1372px;width:185px;height:169px;background:linear-gradient(135deg,#e9e2dc,#a8542e 50%,#6a2c18)}
.service-name{left:423px;top:1370px;font:700 17px "Lato",sans-serif;color:var(--white)}
.service-copy{left:423px;top:1402px;width:560px;font:400 12.5px/22px "Lato",sans-serif;color:#ddd}
.service-meta{top:1514px;font:400 16px "Lato",sans-serif;color:var(--white);display:flex;align-items:center;gap:8px}
.req-btn{left:814px;top:1491px;width:169px;height:45px;background:var(--orange);color:var(--white);font:700 16px/45px "Lato",sans-serif;display:flex;align-items:center;justify-content:center;gap:10px}
.round-arrow{width:38px;height:38px;border-radius:50%;background:#e6e6e6;display:flex;align-items:center;justify-content:center}
/* gallery */
.gal-photo{background:linear-gradient(135deg,#7c7c7c,#a86a4a 45%,#5a3324 80%)}
.gal-focus{left:329px;top:1724px;width:300px;height:249px;border:1px solid #ddd;background:var(--white)}
.gal-focus .inner{position:absolute;left:6px;top:6px;width:286px;height:235px;background:linear-gradient(135deg,#4a4a4a,#5c4a40 50%,#3a3330)}
.gal-arrow{width:0;height:0;border-top:11px solid transparent;border-bottom:11px solid transparent}
/* contact */
.contact{left:0;top:2011px;width:1200px;height:609px;background:linear-gradient(90deg,#6a6a6a 0%,#6e6560 45%,#8a6a52 80%,#a08270 100%)}
.contact-panel{left:162px;top:2127px;width:878px;height:423px;background:var(--panel)}
.address-card{left:187px;top:2152px;width:402px;height:373px;background:var(--white)}
.form-card{left:611px;top:2152px;width:402px;height:373px;background:var(--white)}
.addr-h{left:228px;font:400 21px "Lato",sans-serif;color:var(--ink)}
.addr-line{left:253px;font:400 12px "Lato",sans-serif;color:#555}
.field{left:638px;width:345px;height:37px;border:1px solid var(--line);font:400 11px "Lato",sans-serif;color:#999;padding:11px 14px}
/* social */
.social-btn{top:2731px;width:215px;height:49px;color:var(--white);font:700 18px/49px "Lato",sans-serif;display:flex;align-items:center;justify-content:center;gap:14px;border-radius:2px}
.social-btn i{width:12px;height:12px;background:var(--white);display:block}
.social-count{top:2793px;width:215px;text-align:center;font:400 12.5px "Lato",sans-serif;color:var(--muted)}
/* footer */
.site-footer{left:0;top:2849px;width:1200px;height:78px;background:var(--charcoal);color:#ddd;font:400 11px/78px "Lato",sans-serif}
.site-footer .copy{position:absolute;left:48px}
.site-footer .links{position:absolute;right:42px}
</style>
</head>
<body>

<header class="abs site-header">
  <div class="abs brand">
    <div class="brand-name">CURL RADIANT</div>
    <div class="brand-sub">through and through</div>
  </div>
  <nav class="abs main-nav">
    <a class="active">Home</a><a>Bio</a><a>Services Offered</a><a>Gallery</a><a>Contact Us</a>
  </nav>
  <div class="abs fund-btn">quick fund</div>
</header>

<section class="abs hero" role="img" aria-label="Portrait of a woman with long golden-brown hair and red lips against a dark grey backdrop"></section>
<h1 class="abs hero-title">Curl Radiant through and through by Marisol H</h1>
<p class="abs hero-copy">Lorem ipsum dolor sit amet, consectetur adipiscing elit, sed do eiusmod tempor incididunt ut labore et dolore magna aliqua. Ut enim ad minim veniam, quis nostrud exercitation ullamco laboris nisi ut aliquip ex ea commodo consequat.</p>
<div class="abs hero-btn">REQUEST</div>
<div class="abs dots"><span></span><span></span><span class="on"></span><span></span><span></span></div>

<section class="abs bio">
  <h2>Curl Radiant through and through by Marisol H.</h2>
  <p>Creative. Classic. Distinguished. These are just a few attributes that Marisol embodies. received in depth training from Maple Academy of Hair Design, where I had the opportunity to pair my experience with advanced technical training. My passion for art and design has given me the opportunity to express myself through hair design. I also stay abreast of current trends through industry events, hair shows, and continuing education so that I can offer my clients the best services in hair care, style, and extensions.<span class="bio-more"></span></p>
  <div class="abs bio-portrait" role="img" aria-label="Portrait of the stylist with long honey-blonde hair in a black top"></div>
</section>

<h2 class="abs section-title" style="top:923px">Welcome to Curl Radiant</h2>
<p class="abs welcome-copy">Lorem ipsum dolor sit amet, consectetur adipiscing elit, sed do eiusmod tempor incididunt ut labore et dolore magna aliqua. Ut enim ad minim veniam, quis nostrud exercitation ullamco laboris nisi ut aliquip ex ea commodo consequat. Duis aute irure dolor in reprehenderit in voluptate velit esse cillum dolore eu fugiat nulla pariatur. Excepteur sint occaecat cupidatat non proident, sunt in culpa qui officia deserunt mollit anim id est laborum.</p>
<div class="abs dark-btn" style="left:537px;top:1073px;width:122px;height:37px;line-height:37px">Read More</div>

<section class="abs booking" role="img" aria-label="Soft-focus photo of women with flowing auburn and blonde hair"></section>
<h2 class="abs section-title" style="top:1215px;color:var(--white)">Book an Appointment</h2>
<div class="abs book-panel"></div>
<div class="abs book-pointer"></div>
<div class="abs tabs"><span>Basic Services</span><span>Color Services</span><span>Extensions</span><span>Straitening Services</span></div>
<div class="abs service-photo" role="img" aria-label="Woman with voluminous red curls"></div>
<div class="abs service-name">Cleanse/ Style</div>
<p class="abs service-copy">Lorem ipsum dolor sit amet, consectetur adipiscing elit, sed do eiusmod tempor incididunt ut labore et dolore magna aliqua. Ut enim ad minim veniam, quis nostrud exercitation ullamco laboris nisi ut aliquip ex ea commodo consequat. Ut enim ad minim veniam, quis nostrud exercitation ullamco laboris commodo consequat.</p>
<div class="abs service-meta" style="left:425px"><span style="color:var(--orange);font-weight:700">$</span>45 and up</div>
<div class="abs service-meta" style="left:583px">
  <svg width="15" height="15" viewBox="0 0 16 16"><circle cx="8" cy="8" r="6.5" fill="none" stroke="#c97d1c" stroke-width="2"/><path d="M8 4.5V8l2.5 1.5" fill="none" stroke="#c97d1c" stroke-width="1.8"/></svg>1 hr., 30 min.</div>
<div class="abs req-btn">
  <svg width="17" height="17" viewBox="0 0 16 16"><path d="M1 7.5 15 1 11 15 7.5 9.5Z M7.5 9.5 15 1" fill="none" stroke="#fff" stroke-width="1.6" stroke-linejoin="round"/></svg>Request</div>
<div class="abs round-arrow" style="left:100px;top:1421px"><svg width="12" height="12" viewBox="0 0 12 12"><path d="M8 1 3 6l5 5" fill="none" stroke="#444" stroke-width="2"/></svg></div>
<div class="abs round-arrow" style="left:1052px;top:1421px"><svg width="12" height="12" viewBox="0 0 12 12"><path d="M4 1l5 5-5 5" fill="none" stroke="#444" stroke-width="2"/></svg></div>

<h2 class="abs section-title" style="top:1662px">Our Gallery</h2>
<div class="abs gal-arrow" style="left:31px;top:1824px;border-right:17px solid #aaa"></div>
<div class="abs gal-photo" style="left:72px;top:1750px;width:230px;height:195px" role="img" aria-label="Woman with tousled brunette hair"></div>
<div class="abs gal-focus"><div class="inner" role="img" aria-label="Darkened gallery photo of a woman with brunette hair"></div></div>
<svg class="abs" style="left:441px;top:1811px" width="74" height="74" viewBox="0 0 74 74"><circle cx="37" cy="37" r="37" fill="#6a6a6a" opacity=".9"/><path d="M28 28l18 18M46 46v-8M46 46h-8M30 30h8M30 30v8" fill="none" stroke="#111" stroke-width="4" stroke-linecap="round"/></svg>
<div class="abs gal-photo" style="left:652px;top:1750px;width:230px;height:195px" role="img" aria-label="Woman with tousled brunette hair"></div>
<div class="abs gal-photo" style="left:909px;top:1750px;width:230px;height:195px" role="img" aria-label="Woman with tousled brunette hair"></div>
<div class="abs gal-arrow" style="left:1152px;top:1824px;border-left:17px solid #aaa"></div>

<section class="abs contact" role="img" aria-label="Faded close-up of a woman's flowing reddish-brown hair"></section>
<h2 class="abs section-title" style="top:2056px;color:var(--white)">Contact Us</h2>
<div class="abs contact-panel"></div>
<div class="abs address-card"></div>
<div class="abs addr-h" style="top:2192px">Our Address</div>
<div class="abs addr-line" style="top:2230px">Address line1, Address line2</div>
<div class="abs addr-line" style="top:2258px">Lorem ipsum dolor sit amet</div>
<div class="abs addr-line" style="top:2286px">Country -123456</div>
<div class="abs addr-h" style="top:2317px">Telephones</div>
<div class="abs addr-line" style="top:2352px;left:251px">123 456 7890 (NZ)</div>
<div class="abs addr-line" style="top:2380px;left:251px">123 456 7890 (AU)</div>
<div class="abs addr-h" style="top:2412px">Email Id</div>
<div class="abs addr-line" style="top:2447px;left:257px">info@companyname.com</div>
<div class="abs form-card"></div>
<div class="abs field" style="top:2187px">Name</div>
<div class="abs field" style="top:2246px">Phone</div>
<div class="abs field" style="top:2306px">Email id</div>
<div class="abs field" style="top:2365px;height:86px">Message</div>
<div class="abs dark-btn" style="left:640px;top:2464px;width:119px;height:37px;line-height:37px;font-size:14px;font-weight:400">Send</div>

<h2 class="abs section-title" style="top:2643px;color:var(--navy)">Follow us to Stay in Touch</h2>
<div class="abs social-btn" style="left:80px;background:var(--friend)"><i></i>Friendwall</div>
<div class="abs social-btn" style="left:357px;background:var(--chirp)"><i></i>Chirper</div>
<div class="abs social-btn" style="left:630px;background:var(--link)"><i></i>Linkpro</div>
<div class="abs social-btn" style="left:895px;background:var(--snap)"><i></i>Snapgram</div>
<div class="abs social-count" style="left:80px">1234 Like</div>
<div class="abs social-count" style="left:357px">1234 Followers</div>
<div class="abs social-count" style="left:630px">1234 Followers</div>
<div class="abs social-count" style="left:895px">1234 Followers</div>

<footer class="abs site-footer">
  <span class="copy">Copyright 2016 Comapny Name. All Rights Reserved.</span>
  <span class="links">Policies &nbsp;|&nbsp; Privacy &nbsp;|&nbsp; Terms &amp; Conditions &nbsp;|&nbsp; Disclaimer &nbsp;|&nbsp; Site Map</span>
</footer>

</body>
</html>
```